TwistyLanesCamp.com

Current website needs redesign to make it more attractive and easier to Navigate. Currently being hosted on net porter. Can be accessed at
www,twistylanescamp.com.

```html
<!DOCTYPE html>
<html lang="en">
<head>
<meta charset="utf-8">
<title>TwistyLanesCamp.com</title>
<link href="https://fonts.googleapis.com/css2?family=PT+Sans:wght@400;700&family=Roboto+Condensed:wght@700&family=Arimo:wght@400;700&display=swap" rel="stylesheet">
<style>
:root{
  --red:#c8102e;
  --ink:#141414;
  --text:#555;
  --white:#fff;
  --line:#d9d9d9;
  --footer:#0c0c0c;
}
*{box-sizing:border-box;margin:0;padding:0}
html,body{width:1200px;height:3771px;overflow:hidden}
body{position:relative;background:var(--white);font-family:"PT Sans",sans-serif;color:var(--text)}
.abs{position:absolute}
.btn{position:absolute;display:flex;align-items:center;justify-content:center;background:var(--red);color:var(--white);font-family:"PT Sans",sans-serif;font-weight:700;font-size:14px;border-radius:22px;text-transform:uppercase}
.heading{font-family:"Roboto Condensed",sans-serif;font-weight:700;color:var(--ink);text-transform:uppercase}

/* header */
.topbar{left:473px;top:0;width:727px;height:59px;background:var(--red);color:var(--white);display:flex;align-items:center}
.topbar .phone-icon{margin-left:24px;width:34px;height:34px;border:2px solid var(--white);border-radius:50%;display:flex;align-items:center;justify-content:center}
.topbar .call{margin-left:18px;font-weight:700;font-size:16px}
.topbar .call b{font-size:20px}
.topbar .lang{margin-left:80px;font-weight:700;font-size:13px;display:flex;align-items:center;gap:6px}
.topbar .flag{width:24px;height:16px;background:linear-gradient(#e8e8f0,#c9c9d6);border-radius:2px}
.social{display:flex;gap:8px;margin-left:40px}
.social span{width:26px;height:26px;border-radius:50%;background:rgba(255,255,255,.9)}
.header-strip{left:0;top:0;width:1200px;height:5px;background:var(--red)}
.logo{left:110px;top:66px;font-family:"PT Sans",sans-serif;font-weight:700;font-size:24px;color:var(--ink);display:flex;align-items:center;gap:8px}
.logo i{display:block;width:26px;height:26px;background:var(--red);border-radius:4px}
.nav{left:361px;top:98px;display:flex;gap:21px;font-family:"PT Sans",sans-serif;font-weight:700;font-size:13.5px;color:var(--ink)}
.nav .active{color:var(--red)}
.nav-marker{left:372px;top:128px;width:0;height:0;border-left:8px solid transparent;border-right:8px solid transparent;border-bottom:14px solid var(--red)}

/* hero */
.hero{left:0;top:143px;width:1200px;height:920px;background:linear-gradient(180deg,#cfdbe3 0%,#7f9cae 22%,#5d7d6a 40%,#4f88a6 55%,#3f6f8c 75%,#2d5770 100%)}
.hero-title{left:171px;top:290px;font-size:51px;line-height:52px;color:var(--white)}
.hero .btn{}
.dots{left:566px;top:544px;display:flex;gap:8px}
.dots span{width:12px;height:12px;border-radius:50%;background:var(--white)}
.dots span:first-child{background:var(--red)}
.slides{left:1122px;top:314px;width:40px;color:var(--white);font-weight:700;font-size:14px;text-align:center}
.slides .current{width:40px;height:40px;border-radius:50%;background:var(--white);color:var(--ink);display:flex;align-items:center;justify-content:center}
.slides .rail{width:2px;height:48px;background:var(--white);margin:8px auto 6px}
.slides p{line-height:34px}
.swoosh{left:0;top:0}

/* about */
.about-title{left:0;top:836px;width:1200px;text-align:center;font-size:40px}
.about-copy{left:242px;top:904px;width:716px;text-align:center;font-size:14px;line-height:21.5px}
.about-copy p+p{margin-top:21px}

/* blog */
.blog{left:0;top:1219px;width:1200px;height:1456px;background:linear-gradient(180deg,#e6eff6 0%,#f1f5f8 40%,#eef2ef 100%)}
.blog-title{left:0;top:1312px;width:1200px;text-align:center;font-size:40px}
.photo{position:absolute;border-radius:8px}
.post-title{position:absolute;font-family:"Roboto Condensed",sans-serif;font-weight:700;font-size:20px;line-height:23px;color:var(--ink);text-transform:uppercase;width:440px}
.post-copy{position:absolute;font-size:13px;line-height:21.5px;width:450px}

/* submissions */
.sub-title{left:0;top:2768px;width:1200px;text-align:center;font-size:40px}
.sub-copy{left:250px;top:2838px;width:700px;text-align:center;font-size:14px;line-height:22px}
.frame{left:177px;top:2969px;width:318px;height:293px;border:2px solid var(--red);border-radius:10px}
.field{position:absolute;left:620px;width:466px;border:1px solid var(--line);background:var(--white);font-size:13px;color:#666;padding-left:22px;display:flex;align-items:center}
.field.area{align-items:flex-start;padding-top:24px}

/* footer */
.footer{left:0;top:3452px;width:1200px;height:319px;background:var(--footer);color:var(--white);font-family:"Arimo",sans-serif}
.footer .col{position:absolute;font-size:13.5px;line-height:25px}
.footer h3{font-size:21px;font-weight:700;margin-bottom:14px}
.subscribe{position:absolute;left:579px;top:132px;width:264px;height:40px;background:var(--white);color:#555;font-size:13.5px;display:flex;align-items:center;justify-content:space-between;padding:0 16px}
.footer .contact-btn{position:absolute;left:929px;top:73px;width:136px;height:48px;background:var(--red);font-weight:700;font-size:14px;display:flex;align-items:center;justify-content:center}
.footer .rule{position:absolute;left:110px;top:233px;width:978px;height:1px;background:#333}
.footer .copy{position:absolute;left:0;top:264px;width:1200px;text-align:center;font-size:13.5px}
</style>
</head>
<body>

<header>
  <div class="abs header-strip"></div>
  <div class="abs topbar">
    <div class="phone-icon">
      <svg width="18" height="18" viewBox="0 0 24 24"><path d="M6.6 10.8a15 15 0 0 0 6.6 6.6l2.2-2.2c.3-.3.7-.4 1-.2 1.1.4 2.3.6 3.6.6.6 0 1 .4 1 1V20c0 .6-.4 1-1 1A17 17 0 0 1 3 4c0-.6.4-1 1-1h3.5c.6 0 1 .4 1 1 0 1.3.2 2.5.6 3.6.1.3 0 .7-.2 1z" fill="#fff"/></svg>
    </div>
    <div class="call">Call us Today : <b>+1 888 888 8888</b></div>
    <div class="lang">Eng <svg width="8" height="6" viewBox="0 0 8 6"><path d="M1 1l3 3 3-3" stroke="#fff" fill="none" stroke-width="1.4"/></svg><span class="flag" role="img" aria-label="Language flag"></span></div>
    <div class="social"><span></span><span></span><span></span></div>
  </div>
  <div class="abs logo"><i></i>TwistyLanesCamp.com</div>
  <nav class="abs nav">
    <span class="active">HOME</span><span>ABOUT</span><span>TRAILS &amp; TALES</span><span>THE SMART RVER</span><span>WOMEN ON THE ROAD</span><span>BAD RV</span><span>BLOG</span><span>CONTACT</span>
  </nav>
  <div class="abs nav-marker"></div>
</header>

<section>
  <div class="abs hero" role="img" aria-label="Motorhome parked beside a mountain lake with a picnic table"></div>
  <h1 class="abs heading hero-title">Lessons from<br>the road</h1>
  <div class="btn" style="left:170px;top:414px;width:142px;height:44px">Get Started</div>
  <div class="abs dots"><span></span><span></span><span></span><span></span></div>
  <div class="abs slides">
    <div class="current">1</div>
    <div class="rail"></div>
    <p>2</p><p>3</p><p>4</p>
  </div>
  <svg class="abs swoosh" width="1200" height="1100" viewBox="0 0 1200 1100">
    <path d="M0 880 C250 640 700 560 1200 748 L1200 790 C700 610 260 690 0 925 Z" fill="#0b0b0b"/>
    <path d="M0 925 C260 690 700 610 1200 790 L1200 796 C700 635 265 710 0 955 Z" fill="#fff"/>
    <path d="M0 955 C265 710 700 635 1200 796 L1200 800 C700 672 275 750 0 1040 Z" fill="var(--red)"/>
    <path d="M0 1040 C275 750 700 672 1200 800 L1200 1100 L0 1100 Z" fill="#fff"/>
  </svg>
</section>

<section>
  <h2 class="abs heading about-title">About us</h2>
  <div class="abs about-copy">
    <p>My wife and I have been RVing since 2007. We have had two Super C’s and two Class A motor homes. We are not full timers but we have spent a lot of time on the road.</p>
    <p>Like many of you, we started cold. No lessons and very little in the way of education from the RV dealers who sold us our coaches. Our first RV initiation was done in 20 minutes by a drunken employee who barely made it through his all too brief “brief”. But there we were. Naively happy. Little did we know that there was much to learn before we could smooth out the bumps on the road to adventure.</p>
  </div>
  <div class="btn" style="left:528px;top:1073px;width:144px;height:44px">Learn More</div>
</section>

<section>
  <div class="abs blog" role="img" aria-label="Faint sky and mountain backdrop"></div>
  <h2 class="abs heading blog-title">Featured blog posts</h2>

  <div class="photo" style="left:111px;top:1397px;width:489px;height:295px;background:linear-gradient(180deg,#9cc3dd 0%,#6f9d58 45%,#3f6b2e 100%)" role="img" aria-label="Camper van beside a calm lake under green hills"></div>
  <div class="post-title" style="left:638px;top:1441px">Bad RV</div>
  <div class="post-copy" style="left:638px;top:1486px">We serve as an advocacy forum for other RVers seeking advice and remediation against both dealers and manufacturers who fail to meet their customer obligations. “Bad RV” is dedicated to helping you avoid some of these...</div>
  <div class="btn" style="left:641px;top:1601px;width:143px;height:44px">Read More</div>

  <div class="post-title" style="left:111px;top:1735px">RV envy? Why you will always want a different one!</div>
  <div class="post-copy" style="left:111px;top:1801px">When my wife and I settle into a campground, we like to walk around and look at other rigs.&nbsp; If the owners are outside, we often ask them how they like their RV.&nbsp; At one...</div>
  <div class="btn" style="left:114px;top:1896px;width:143px;height:44px">Read More</div>
  <div class="photo" style="left:600px;top:1692px;width:487px;height:294px;background:linear-gradient(135deg,#b7c4cc 0%,#8a99a6 40%,#c9b8a0 70%,#6f7f59 100%)" role="img" aria-label="Family relaxing in camp chairs beside their RV"></div>

  <div class="photo" style="left:111px;top:1986px;width:489px;height:288px;background:linear-gradient(180deg,#4f8fd0 0%,#a9c9e6 40%,#dfe4e6 60%,#7c9a5a 100%)" role="img" aria-label="White motorhome parked on a grassy coastal hill"></div>
  <div class="post-title" style="left:638px;top:2024px">Class A motorhomes: prepare for a love hate relationship</div>
  <div class="post-copy" style="left:638px;top:2087px">My wife and I have owned two class A motorhomes: one a new 37 ft. gas coach and a new 40 ft. bath and half diesel pusher. Since we successfully sued the manufacturers of both...</div>
  <div class="btn" style="left:641px;top:2184px;width:143px;height:44px">Read More</div>

  <div class="post-title" style="left:111px;top:2318px">RV hell: driving off without your wife!</div>
  <div class="post-copy" style="left:111px;top:2370px">It was a steady downpour that day in rural Mississippi. We were on a four-lane highway in our Vista 36 FK towing our dozer yellow Ridgeback 4x4.&nbsp; We had been having trouble with our automatic...</div>
  <div class="btn" style="left:114px;top:2479px;width:143px;height:44px">Read More</div>
  <div class="photo" style="left:600px;top:2274px;width:487px;height:296px;background:linear-gradient(160deg,#3a5e86 0%,#a9b8c4 35%,#d9b98a 55%,#5a4a3c 80%,#2f2a26 100%)" role="img" aria-label="Camper van by rugged mountains at sunset"></div>
</section>

<section>
  <h2 class="abs heading sub-title">Trails and tales submissions</h2>
  <p class="abs sub-copy">Please feel free to share your RV adventure by sending us your story here. We may choose to include it on our website in our Trails and Tales section!</p>
  <div class="photo" style="left:262px;top:2899px;width:316px;height:290px;background:linear-gradient(180deg,#8f9a86 0%,#4d5a3c 50%,#2e3428 100%)" role="img" aria-label="RV parked among trees at dusk"></div>
  <div class="photo" style="left:111px;top:3060px;width:316px;height:290px;background:linear-gradient(180deg,#3f8fd6 0%,#c98a5c 40%,#8a5a3a 65%,#5f5a52 100%)" role="img" aria-label="Motor coach on a highway beneath red rock cliffs"></div>
  <div class="abs frame"></div>

  <div class="field" style="top:2902px;height:69px">Your Name</div>
  <div class="field" style="top:2993px;height:69px">Your Email</div>
  <div class="field" style="top:3084px;height:69px;justify-content:space-between;padding-right:18px">Upload your Image
    <svg width="16" height="13" viewBox="0 0 16 13"><rect x="1" y="1" width="14" height="11" fill="none" stroke="#555"/><path d="M3 10l3-4 2 2 2-3 3 5z" fill="#555"/></svg>
  </div>
  <div class="field area" style="top:3173px;height:165px">Tell Us Your Story</div>
  <div class="btn" style="left:934px;top:3284px;width:142px;height:46px;border-radius:0">Read More</div>
</section>

<footer class="abs footer">
  <div class="col" style="left:110px;top:73px">
    <h3>Links</h3>
    <div>Contact us</div><div style="margin-top:-5px">Privacy policy</div><div style="margin-top:-5px">Terms &amp; condition</div>
  </div>
  <div class="col" style="left:336px;top:78px">
    <div>Help</div><div>About us</div><div>Service</div><div>Blog</div><div>Bad RV</div>
  </div>
  <div class="col" style="left:577px;top:78px">
    <div>Hungry for more?</div><div>Signup for free shipping</div>
  </div>
  <div class="subscribe">Email address
    <svg width="16" height="16" viewBox="0 0 16 16"><path d="M15 1L1 7l5 2 2 6z" fill="var(--red)"/></svg>
  </div>
  <div class="contact-btn">CONTACT US</div>
  <div class="col" style="left:933px;top:151px">
    <div>info@companyname.com</div><div>+1 888 888 8888</div>
  </div>
  <div class="rule"></div>
  <div class="copy">© &nbsp;Copyrights 2021 Company name | All Rights Reserved</div>
</footer>

</body>
</html>
```